PPT company presentation (energy saving motors)

We need a modern PowerPoint layout for our company. We are a familiy owned company which is located in Germany. We develop custom specified applications in the field of drive technology.
The new design should be more friendly, bright and professional as the old version (attached as pdf). More company Information: www.brovatek.de

It Company

```html
<!DOCTYPE html>
<html lang="en">
<head>
<meta charset="utf-8">
<title>Brovatek – Presentation Layout</title>
<link rel="stylesheet" href="https://fonts.googleapis.com/css2?family=Montserrat:wght@400;600;700;800&family=Open+Sans:wght@400;600&display=swap">
<style>
:root{
  --green:#1f9a4b;
  --green-dark:#15763a;
  --green-light:#7cc896;
  --grey:#8d9591;
  --grey-light:#e4e8e6;
  --ink:#3c4240;
  --paper:#ffffff;
  --backdrop:#ece9e4;
}
*{box-sizing:border-box;margin:0;padding:0}
html,body{width:800px;height:1200px;overflow:hidden}
body{background:var(--backdrop);font-family:"Open Sans",Arial,sans-serif;color:var(--ink);position:relative}
.slide{position:absolute;width:214px;height:120px;background:var(--paper);box-shadow:0 2px 5px rgba(0,0,0,.25);overflow:hidden}
.col-left{left:173px}.col-right{left:400px}
.slide-title{position:absolute;left:12px;top:9px;font:700 8px "Montserrat",sans-serif;color:var(--ink);letter-spacing:.4px;text-transform:uppercase}
.footer-mark{position:absolute;left:8px;bottom:5px;font:700 6px "Montserrat",sans-serif;color:var(--green)}
.footer-line{position:absolute;left:0;right:0;bottom:0;height:2px;background:var(--green)}
.photo{position:absolute;background:linear-gradient(135deg,#9bb4a8,#5d7468)}
.label{position:absolute;font:700 7px "Montserrat",sans-serif;color:#fff;text-transform:uppercase}
.small{font-size:4.5px;line-height:1.35;color:var(--grey)}
svg{position:absolute;left:0;top:0}
/* cover */
.cover{left:240px;top:25px;width:320px;height:175px}
.cover-band{position:absolute;left:0;right:0;bottom:0;height:24px;background:var(--green)}
.cover-name{position:absolute;left:0;right:0;top:62px;text-align:center;font:700 30px "Montserrat",sans-serif;color:var(--green)}
.cover-band span{position:absolute;top:8px;font:600 6px "Open Sans",sans-serif;color:#fff}
/* thank you */
.thanks{left:235px;top:1000px;width:330px;height:170px;background:var(--green)}
.thanks-title{position:absolute;left:0;right:0;top:38px;text-align:center;font:800 32px "Montserrat",sans-serif;color:#fff;letter-spacing:2px}
.contact{position:absolute;top:112px;width:80px;text-align:center;color:#fff;font-size:5px;line-height:1.3}
.contact .icon{width:16px;height:16px;border-radius:50%;background:#fff;margin:0 auto 4px;position:relative}
</style>
</head>
<body>

<section class="slide cover">
  <div class="cover-name">Brovatek</div>
  <div class="cover-band">
    <span style="left:14px">www.brovatek.de</span>
    <span style="right:14px">Company Presentation</span>
  </div>
</section>

<section class="slide col-left" style="top:213px">
  <div class="photo" role="img" aria-label="Team photo of hands joined together" style="left:0;top:0;width:150px;height:64px"></div>
  <div class="photo" role="img" aria-label="Office teamwork photo" style="left:152px;top:0;width:62px;height:64px;background:linear-gradient(135deg,#c7b9a0,#7c8a82)"></div>
  <div style="position:absolute;left:0;top:44px;width:60px;height:14px;background:var(--green)"></div>
  <div class="label" style="left:8px;top:47px">Profile</div>
  <div class="small" style="position:absolute;left:10px;top:72px;width:190px">Family owned company developing custom drive applications since many years.</div>
  <div class="footer-mark">Brovatek</div><div class="footer-line"></div>
</section>

<section class="slide col-right" style="top:213px">
  <div class="slide-title">Why our firm</div>
  <div class="photo" role="img" aria-label="Workshop photo" style="left:10px;top:24px;width:60px;height:40px;background:linear-gradient(135deg,#d9c3a3,#9a8e7b)"></div>
  <div class="photo" role="img" aria-label="Meeting photo" style="left:76px;top:24px;width:60px;height:40px"></div>
  <div class="photo" role="img" aria-label="Engineering photo" style="left:142px;top:24px;width:60px;height:40px;background:linear-gradient(135deg,#b8c8d6,#6f8496)"></div>
  <div class="small" style="position:absolute;left:10px;top:72px;width:190px">Quality, reliability and energy saving drive solutions.</div>
  <div class="footer-mark">Brovatek</div><div class="footer-line"></div>
</section>

<section class="slide col-left" style="top:340px">
  <div class="photo" role="img" aria-label="Photo of business people" style="left:0;top:0;width:214px;height:120px;background:linear-gradient(135deg,#b9c4be,#6e7e77)"></div>
  <div style="position:absolute;left:0;right:0;top:62px;height:22px;background:var(--green)"></div>
  <div class="label" style="left:120px;top:66px;font-size:12px">Profile</div>
</section>

<section class="slide col-right" style="top:340px">
  <div class="slide-title">Our management team</div>
  <div class="photo" role="img" aria-label="Portrait of manager" style="left:38px;top:32px;width:36px;height:40px"></div>
  <div class="photo" role="img" aria-label="Portrait of manager" style="left:89px;top:32px;width:36px;height:40px"></div>
  <div class="photo" role="img" aria-label="Portrait of manager" style="left:140px;top:32px;width:36px;height:40px"></div>
  <div class="small" style="position:absolute;left:30px;top:78px;width:160px;display:flex;justify-content:space-between"><span>Name One</span><span>Name Two</span><span>Name Three</span></div>
  <div class="footer-mark">Brovatek</div><div class="footer-line"></div>
</section>

<section class="slide col-left" style="top:470px">
  <div class="slide-title">Today's agenda</div>
  <svg width="214" height="120" viewBox="0 0 214 120">
    <circle cx="40" cy="58" r="14" fill="var(--green)"/>
    <circle cx="82" cy="58" r="14" fill="var(--grey)"/>
    <circle cx="124" cy="58" r="14" fill="var(--green-light)"/>
    <circle cx="166" cy="58" r="14" fill="var(--grey)"/>
    <g font-family="Open Sans" font-size="4.5" fill="#8d9591" text-anchor="middle">
      <text x="40" y="84">Intro</text><text x="82" y="84">Products</text><text x="124" y="84">Market</text><text x="166" y="84">Outlook</text>
    </g>
  </svg>
  <div class="footer-mark">Brovatek</div><div class="footer-line"></div>
</section>

<section class="slide col-right" style="top:470px">
  <div class="slide-title">Key points</div>
  <svg width="214" height="120" viewBox="0 0 214 120">
    <polygon points="170,0 214,0 214,60 150,120 120,120" fill="var(--green)"/>
    <polygon points="190,0 214,0 214,25" fill="var(--green-dark)"/>
    <g fill="var(--grey)"><circle cx="20" cy="38" r="4"/><circle cx="20" cy="55" r="4"/><circle cx="20" cy="72" r="4"/><circle cx="20" cy="89" r="4"/></g>
    <g fill="var(--grey-light)"><rect x="30" y="36" width="90" height="4"/><rect x="30" y="53" width="80" height="4"/><rect x="30" y="70" width="95" height="4"/><rect x="30" y="87" width="70" height="4"/></g>
  </svg>
  <div class="footer-mark">Brovatek</div>
</section>

<section class="slide col-left" style="top:600px">
  <div class="slide-title">Our promises</div>
  <svg width="214" height="120" viewBox="0 0 214 120">
    <circle cx="85" cy="45" r="18" fill="none" stroke="var(--grey)" stroke-width="1.5"/>
    <circle cx="120" cy="45" r="18" fill="none" stroke="var(--grey)" stroke-width="1.5"/>
    <circle cx="102" cy="75" r="18" fill="var(--green)"/>
    <g font-family="Open Sans" font-size="4.5" fill="#8d9591"><text x="20" y="45">Quality</text><text x="150" y="45">Service</text><text x="130" y="90">Efficiency</text></g>
  </svg>
  <div class="footer-mark">Brovatek</div><div class="footer-line"></div>
</section>

<section class="slide col-right" style="top:600px">
  <div class="slide-title">Our commitment</div>
  <svg width="214" height="120" viewBox="0 0 214 120">
    <rect x="20" y="36" width="120" height="8" fill="var(--green)"/>
    <rect x="20" y="52" width="90" height="8" fill="var(--grey)"/>
    <rect x="20" y="68" width="150" height="8" fill="var(--green-light)"/>
    <rect x="20" y="84" width="70" height="8" fill="var(--grey)"/>
  </svg>
  <div class="footer-mark">Brovatek</div><div class="footer-line"></div>
</section>

<section class="slide col-left" style="top:728px">
  <div class="slide-title">Some points for a good meeting</div>
  <svg width="214" height="120" viewBox="0 0 214 120">
    <rect x="14" y="34" width="160" height="9" fill="var(--green)"/>
    <rect x="14" y="49" width="130" height="9" fill="var(--grey-light)"/>
    <rect x="14" y="64" width="150" height="9" fill="var(--green)"/>
    <rect x="14" y="79" width="110" height="9" fill="var(--grey-light)"/>
  </svg>
  <div class="footer-mark">Brovatek</div><div class="footer-line"></div>
</section>

<section class="slide col-right" style="top:728px">
  <div class="slide-title">Company report charts</div>
  <svg width="214" height="120" viewBox="0 0 214 120">
    <line x1="20" y1="95" x2="200" y2="95" stroke="var(--grey-light)"/>
    <g fill="var(--grey)">
      <rect x="28" y="78" width="9" height="17"/><rect x="58" y="70" width="9" height="25"/><rect x="88" y="62" width="9" height="33"/><rect x="118" y="52" width="9" height="43"/><rect x="148" y="44" width="9" height="51"/><rect x="178" y="34" width="9" height="61"/>
    </g>
    <g fill="var(--green)">
      <rect x="38" y="72" width="9" height="23"/><rect x="68" y="64" width="9" height="31"/><rect x="98" y="56" width="9" height="39"/><rect x="128" y="46" width="9" height="49"/><rect x="158" y="38" width="9" height="57"/><rect x="188" y="28" width="9" height="67"/>
    </g>
  </svg>
  <div class="footer-mark">Brovatek</div>
</section>

<section class="slide col-left" style="top:858px">
  <div class="slide-title">Sales chart</div>
  <svg width="214" height="120" viewBox="0 0 214 120">
    <line x1="14" y1="95" x2="200" y2="95" stroke="var(--grey-light)"/>
    <g fill="var(--green)">
      <rect x="20" y="70" width="6" height="25"/><rect x="40" y="55" width="6" height="40"/><rect x="60" y="62" width="6" height="33"/><rect x="80" y="45" width="6" height="50"/><rect x="100" y="58" width="6" height="37"/><rect x="120" y="40" width="6" height="55"/><rect x="140" y="50" width="6" height="45"/><rect x="160" y="36" width="6" height="59"/><rect x="180" y="46" width="6" height="49"/>
    </g>
    <g fill="var(--grey)">
      <rect x="27" y="78" width="6" height="17"/><rect x="47" y="66" width="6" height="29"/><rect x="67" y="72" width="6" height="23"/><rect x="87" y="60" width="6" height="35"/><rect x="107" y="68" width="6" height="27"/><rect x="127" y="55" width="6" height="40"/><rect x="147" y="62" width="6" height="33"/><rect x="167" y="50" width="6" height="45"/><rect x="187" y="58" width="6" height="37"/>
    </g>
    <polyline points="23,60 43,48 63,54 83,38 103,50 123,32 143,44 163,28 183,38" fill="none" stroke="var(--green-dark)" stroke-width="1"/>
  </svg>
  <div class="footer-mark">Brovatek</div><div class="footer-line"></div>
</section>

<section class="slide col-right" style="top:858px">
  <div class="slide-title">Positive or negative?</div>
  <svg width="214" height="120" viewBox="0 0 214 120">
    <g fill="none" stroke-width="7">
      <circle cx="50" cy="62" r="18" stroke="var(--grey-light)"/>
      <circle cx="50" cy="62" r="18" stroke="var(--green)" stroke-dasharray="85 113" transform="rotate(-90 50 62)"/>
      <circle cx="107" cy="62" r="18" stroke="var(--grey-light)"/>
      <circle cx="107" cy="62" r="18" stroke="var(--green)" stroke-dasharray="60 113" transform="rotate(-90 107 62)"/>
      <circle cx="164" cy="62" r="18" stroke="var(--grey-light)"/>
      <circle cx="164" cy="62" r="18" stroke="var(--green)" stroke-dasharray="95 113" transform="rotate(-90 164 62)"/>
    </g>
    <g font-family="Montserrat" font-weight="700" font-size="6" fill="#3c4240" text-anchor="middle">
      <text x="50" y="64">75%</text><text x="107" y="64">53%</text><text x="164" y="64">84%</text>
    </g>
  </svg>
  <div class="footer-mark">Brovatek</div><div class="footer-line"></div>
</section>

<section class="slide thanks">
  <div class="thanks-title">THANK YOU!</div>
  <div class="contact" style="left:25px"><div class="icon"><svg width="16" height="16" viewBox="0 0 16 16"><path d="M8 3a3 3 0 0 0-3 3c0 2.5 3 6 3 6s3-3.5 3-6a3 3 0 0 0-3-3z" fill="var(--green)"/></svg></div>Musterstraße 1<br>Germany</div>
  <div class="contact" style="left:125px"><div class="icon"><svg width="16" height="16" viewBox="0 0 16 16"><path d="M5 4l2 2-1 1a6 6 0 0 0 3 3l1-1 2 2-1.5 1.5C7 12 4 9 3.5 5.5z" fill="var(--green)"/></svg></div>+49 000 000000</div>
  <div class="contact" style="left:225px"><div class="icon"><svg width="16" height="16" viewBox="0 0 16 16"><circle cx="8" cy="8" r="4" fill="none" stroke="var(--green)" stroke-width="1.5"/></svg></div>www.brovatek.de</div>
</section>

</body>
</html>
```